WP website design for Pelton

We need a wordpress design that will incorporate a professional color scheme with company logo in a clean layout. The design needs to consider that this will be developed on a responsive theme. Colors are will be the green of the logo and any others that will creatively highlight it.

Industry/Entity Type

It Company

Font styles to use
Sans Serif

Requirements
Must have
• Navigation: 1) Home 2) Auctions 3) Auction Services 4) Sellers 5) RK Pelton Livestock 6) About Us 7) Contact Us
Site will have slideshow element, image attached.
Widgets will be: 1)Email Signup form 2) Featured Auctions widget 3) Social Media (Chirply, Vidloop, RSS) 4) News & Events blog
Footer will have smaller company logo, association logos (attached) and contact info (below)
▪ R.K. Pelton Inc. / Auctioneers
▪ 4716 NC Hwy 91
▪ Marbury, NC 27604
▪ Office: (252) 555-0184
▪ Cell: (252) 555-0137
▪ email: rkpelton@rkpelton-example.com
Nice to have
• Site will have drop-down menus - please indicate the styling, for instance the dropdown menus

```html
<!DOCTYPE html>
<html lang="en">
<head>
<meta charset="utf-8">
<title>R.K. Pelton Inc. / Auctioneers</title>
<link href="https://fonts.googleapis.com/css2?family=Arimo:wght@400;700&family=Cinzel:wght@400;700&family=Open+Sans:wght@400;600;700&display=swap" rel="stylesheet">
<style>
:root{
  --green:#3d8c1f;
  --green-dark:#2e7414;
  --green-light:#6cc04a;
  --text:#333;
  --muted:#555;
  --panel:#fff;
  --page:#f3f3f3;
  --footer:#4a4a4a;
  --dark-btn:#2b2b2b;
}
*{margin:0;padding:0;box-sizing:border-box}
html,body{width:917px;height:1200px;overflow:hidden}
body{position:relative;background:var(--page);font-family:Arimo,Arial,sans-serif;color:var(--text)}
.abs{position:absolute}
.header{left:0;top:0;width:917px;height:113px;background:#fff}
.brand{left:78px;top:30px;color:var(--green);font-family:Arimo,Arial,sans-serif;font-size:17px;line-height:22px;display:flex;align-items:center;gap:8px}
.brand-dot{width:12px;height:12px;border-radius:50%;background:var(--green)}
.follow{left:640px;top:55px;font-size:18px;color:#333;font-family:Arimo,Arial,sans-serif}
.social{top:53px;width:28px;height:28px;border-radius:50%;color:#fff;font-size:7px;display:flex;align-items:center;justify-content:center;font-weight:700}
.social.chirply{left:735px;background:#3b5aa0}
.social.vidloop{left:773px;background:#d52b1e}
.social.rss{left:812px;background:#e9902a}
.nav{left:0;top:113px;width:917px;height:31px;background:var(--green);display:flex;padding-left:75px}
.nav a{color:#fff;text-decoration:none;font-size:12px;height:31px;line-height:30px;padding:0 26px;border-right:1px solid #2f7214;position:relative}
.nav a:last-child{border-right:none}
.nav a.current{border-bottom:2px solid #fff}
.hero{left:0;top:144px;width:917px;height:341px;background:linear-gradient(#e9f1f6 0%,#d7dde0 18%,#8d7a5a 32%,#c79a55 48%,#b5893e 55%,#6f6a4a 68%,#a59360 80%,#6f7f3a 100%)}
.hero-band{left:0;top:440px;width:917px;height:45px;background:linear-gradient(#5aa235,#3f8a1f)}
.hero-caption{left:0;top:450px;width:917px;text-align:center;color:#fff;font-size:13.5px;letter-spacing:.2px}
.dots{left:420px;top:470px;display:flex;gap:7px}
.dots span{width:8px;height:8px;border-radius:50%;background:#fff}
.dots span.on{background:#e11b1b}
.panel{left:76px;top:485px;width:764px;height:602px;background:var(--panel);box-shadow:0 0 4px rgba(0,0,0,.15)}
.welcome{left:76px;top:512px;width:764px;text-align:center;font-family:Cinzel,Georgia,serif;font-size:19px;color:#333}
.welcome b{color:var(--green);font-weight:400}
.intro{left:82px;top:558px;width:752px;text-align:center;font-size:10.5px;line-height:18px;color:#333}
.h-section{font-family:Cinzel,Georgia,serif;font-size:19px;color:var(--green);font-weight:400}
.thumb{width:95px;height:63px;border:2px solid #fff;box-shadow:0 0 2px rgba(0,0,0,.35);background:linear-gradient(#8db8dd 0%,#bcd3e6 35%,#8c7d62 55%,#6b8f4a 100%)}
.item-title{font-size:10.8px;letter-spacing:.4px;color:#222}
.item-type{font-size:10.5px;color:var(--green)}
.item-meta{font-size:9.6px;color:#333;line-height:15.5px}
.item-meta b{font-weight:700}
.item-text{width:304px;font-size:9.8px;line-height:14.6px;text-align:justify;color:#333}
.btn{width:76px;height:23px;border-radius:3px;color:#fff;font-family:"Open Sans",Arial,sans-serif;font-size:10px;font-weight:600;display:flex;align-items:center;gap:7px;padding-left:11px}
.btn.details{background:var(--green)}
.btn.gallery{background:var(--dark-btn)}
.btn svg{flex:none}
.signup{left:593px;top:666px;width:230px;height:191px;border-radius:3px;background:linear-gradient(var(--green-light),var(--green-dark))}
.signup h3{position:absolute;left:17px;top:13px;font-family:Cinzel,Georgia,serif;font-size:17px;font-weight:400;color:#333}
.signup h3 b{color:#fff;font-weight:400}
.signup p{position:absolute;left:20px;top:38px;width:200px;font-family:"Open Sans",Arial,sans-serif;font-size:9px;line-height:12px;color:#fff}
.field{position:absolute;left:20px;width:187px;height:22px;background:#fff;border:1px solid #cfcfcf;font-size:9.5px;color:#888;padding:5px 6px}
.subscribe{position:absolute;left:19px;top:154px;width:105px;height:26px;border-radius:13px;background:#fff;border:2px solid #555;font-family:"Open Sans",Arial,sans-serif;font-size:10px;font-weight:700;color:#222;text-align:center;line-height:22px}
.news-thumb{width:52px;height:38px;border:2px solid #fff;box-shadow:0 0 2px rgba(0,0,0,.35);background:linear-gradient(135deg,#3f79b8,#c9a577)}
.news-text{width:172px;font-size:9.6px;line-height:14.4px;color:#333}
.more{font-size:9.5px;font-weight:700;color:var(--green);text-align:right;width:200px}
.footer{left:0;top:1087px;width:917px;height:113px;background:var(--footer)}
.contact{left:84px;top:1104px;font-size:11px;line-height:15.4px;color:#fff}
.badge{top:1128px;background:#bdbdbd}
.footer-brand{left:736px;top:1138px;color:#e8e8e8;font-size:12.5px;display:flex;align-items:center;gap:6px}
.footer-brand span.sq{width:10px;height:10px;background:#e8e8e8}
</style>
</head>
<body>
<header class="abs header"></header>
<div class="abs brand"><span class="brand-dot"></span><span>R.K. Pelton Inc. / Auctioneers</span></div>
<div class="abs follow">Follow Us:</div>
<div class="abs social chirply">Chirply</div>
<div class="abs social vidloop">Vidloop</div>
<div class="abs social rss">
  <svg width="14" height="14" viewBox="0 0 14 14"><circle cx="2.5" cy="11.5" r="2" fill="#fff"/><path d="M1 6a7 7 0 0 1 7 7M1 1.5a11.5 11.5 0 0 1 11.5 11.5" stroke="#fff" stroke-width="2" fill="none"/></svg>
</div>

<nav class="abs nav">
  <a class="current">Home</a><a>Auctions</a><a>Auction Services</a><a>Sellers</a><a>RK Pelton Livestock</a><a>About Us</a><a>Contact Us</a>
</nav>

<div class="abs hero" role="img" aria-label="Slideshow photo: autumn pond reflecting bare trees and a golden field"></div>
<div class="abs hero-band" role="img" aria-label="Grass strip beneath the slideshow"></div>
<div class="abs hero-caption">LOREM IPSUM DOLOR SIT AMET, CONSECTETUR</div>
<div class="abs dots"><span class="on"></span><span></span><span></span><span></span></div>

<main class="abs panel"></main>
<h1 class="abs welcome"><b>WELCOME</b> TO R.K.PELTON</h1>
<p class="abs intro">Lorem ipsum dolor sit amet, consectetur adipiscing elit, sed do eiusmod tempor incididunt ut labore et dolore magna aliqua. Ut enim ad minim veniam, quis nostrud exercitation ullamco laboris nisi ut aliquip ex ea commodo consequat. Duis aute irure dolor in reprehenderit in voluptate velit esse cillum dolore eu fugiat nulla pariatur. Excepteur sint occaecat cupidatat non proident, sunt in culpa qui officia deserunt mollit...</p>

<h2 class="abs h-section" style="left:94px;top:668px">FEATURED AUCTIONS</h2>

<!-- auction 1 -->
<div class="abs thumb" style="left:92px;top:710px" role="img" aria-label="Photo of the auction property, a two-storey house"></div>
<div class="abs item-title" style="left:200px;top:711px">SHOP EQUIPMENT/TOOLS * PORK PROCESSING ITEMS</div>
<div class="abs item-type" style="left:200px;top:729px">LIVE ON-SITE AUCTION</div>
<div class="abs item-meta" style="left:200px;top:743px"><b>Begins:</b>&nbsp; Saturday, March 16, 2013 at 10:00 AM EDT<br><b>Location:</b>&nbsp; 2890 Alder Road Fenwick, KY 40071</div>
<div class="abs btn details" style="left:94px;top:789px"><svg width="20" height="9"><rect width="8" height="9" rx="1" fill="#fff"/><rect x="10" y="1" width="10" height="1.6" fill="#fff"/><rect x="10" y="4" width="10" height="1.6" fill="#fff"/><rect x="10" y="7" width="10" height="1.6" fill="#fff"/></svg>Details</div>
<div class="abs btn gallery" style="left:94px;top:821px"><svg width="14" height="12"><rect x="1" y="2" width="11" height="9" fill="none" stroke="#fff" stroke-width="1.4"/><path d="M2 10l3-4 3 3 2-2 2 3z" fill="#fff"/></svg>Gallery</div>
<p class="abs item-text" style="left:200px;top:786px">Lorem ipsum dolor sit amet, consectetur adipiscing elit, sed do eiusmod tempor incididunt ut labore et dolore magna aliqua. Ut enim pariatur. Excepteur sint occaecat cupidatat non proident, sunt in culpa qui officia deserunt mollit anim id est laborum.</p>

<!-- auction 2 -->
<div class="abs thumb" style="left:92px;top:897px" role="img" aria-label="Photo of the auction property, a two-storey house"></div>
<div class="abs item-title" style="left:200px;top:898px">SHOP EQUIPMENT/TOOLS * PORK PROCESSING ITEMS</div>
<div class="abs item-type" style="left:200px;top:916px">LIVE ON-SITE AUCTION</div>
<div class="abs item-meta" style="left:200px;top:930px"><b>Begins:</b>&nbsp; Saturday, March 16, 2013 at 10:00 AM EDT<br><b>Location:</b>&nbsp; 2890 Alder Road Fenwick, KY 40071</div>
<div class="abs btn details" style="left:94px;top:976px"><svg width="20" height="9"><rect width="8" height="9" rx="1" fill="#fff"/><rect x="10" y="1" width="10" height="1.6" fill="#fff"/><rect x="10" y="4" width="10" height="1.6" fill="#fff"/><rect x="10" y="7" width="10" height="1.6" fill="#fff"/></svg>Details</div>
<div class="abs btn gallery" style="left:94px;top:1008px"><svg width="14" height="12"><rect x="1" y="2" width="11" height="9" fill="none" stroke="#fff" stroke-width="1.4"/><path d="M2 10l3-4 3 3 2-2 2 3z" fill="#fff"/></svg>Gallery</div>
<p class="abs item-text" style="left:200px;top:973px">Lorem ipsum dolor sit amet, consectetur adipiscing elit, sed do eiusmod tempor incididunt ut labore et dolore magna aliqua. Ut enim pariatur. Excepteur sint occaecat cupidatat non proident, sunt in culpa qui officia deserunt mollit anim id est laborum.</p>

<!-- signup -->
<form class="abs signup">
  <h3>EMAIL <b>SIGNUP</b> FORM</h3>
  <p>Lorem ipsum dolor sit amet, consectetuer adipiscing elit. Nam</p>
  <div class="field" style="top:76px">Your Name</div>
  <div class="field" style="top:115px">Email Address</div>
  <div class="subscribe">Subscribe Now</div>
</form>

<!-- news -->
<h2 class="abs h-section" style="left:597px;top:893px">NEWS &amp; EVENT BLOG</h2>
<div class="abs news-thumb" style="left:597px;top:923px" role="img" aria-label="Blog post photo: house with a sold sign"></div>
<p class="abs news-text" style="left:658px;top:920px">Lorem ipsum dolor sit amet, consctetur adipiscing elit, sed do eiusmod tempor incididuntmagna aliqua.</p>
<div class="abs more" style="left:624px;top:968px">more details...</div>
<div class="abs news-thumb" style="left:597px;top:996px" role="img" aria-label="Blog post photo: house with a sold sign"></div>
<p class="abs news-text" style="left:658px;top:993px">Lorem ipsum dolor sit amet, consctetur adipiscing elit, sed do eiusmod tempor incididuntmagna aliqua.</p>
<div class="abs more" style="left:624px;top:1041px">more details...</div>

<footer class="abs footer"></footer>
<address class="abs contact" style="font-style:normal">R.K. Pelton Inc. / Auctioneers<br>4716 NC Hwy 91 Marbury, NC 27604<br>Office: (252) 555-0184<br>Cell: (252) 555-0137<br>email: rkpelton@rkpelton-example.com</address>
<div class="abs badge" style="left:565px;top:1136px;width:55px;height:22px;border-radius:3px"></div>
<div class="abs badge" style="left:628px;top:1133px;width:38px;height:28px;border-radius:4px"></div>
<div class="abs badge" style="left:679px;top:1128px;width:38px;height:38px;border-radius:50%"></div>
<div class="abs footer-brand"><span class="sq"></span><span>R.K. Pelton Inc.<br>/ Auctioneers</span></div>
</body>
</html>
```